Media Training Presentation (template)

This is a 49-slide power point deck to be used in training clients to deal with the media in various settings. We need a template we can personalize for different clients. The overall color scheme should match our logo. It should look very professional, but also engaging. The word doc contains all of the text, images, and videos for each slide. Also uploaded our logo. Please match/coordinate colors of presentation to the logo colors. If you prefer, you can submit five or six slides showing the overall design and a template for each type of slide, then complete the remainder of the slides within 24 hours if chosen. (Sorry for the quick turnaround…we didn’t know we would need it this quickly!) Thanks for submitting!
Target Market(s)
Government and corporate clients
Look and feel

```html
<!DOCTYPE html>
<html lang="en">
<head>
<meta charset="utf-8">
<title>Media Training Deck</title>
<link href="https://fonts.googleapis.com/css2?family=Montserrat:wght@400;600;700&family=Roboto:wght@700&display=swap" rel="stylesheet">
<style>
:root{
  --brand-blue:#0a57ae;
  --ink-gray:#5c5f63;
  --rule-blue:#3a6fb8;
  --page-bg:#e4e5e7;
  --slide-bg:#ffffff;
}
*{margin:0;padding:0;box-sizing:border-box}
html,body{width:1200px;height:931px;overflow:hidden;background:var(--page-bg)}
body{font-family:"Montserrat",sans-serif;position:relative}
.slide{position:absolute;width:377px;height:212px;background:var(--slide-bg);box-shadow:0 2px 6px rgba(0,0,0,.25);overflow:hidden}
.c1{left:26px}.c2{left:414px}.c3{left:803px}
.r1{top:26px}.r2{top:250px}.r3{top:473px}.r4{top:696px}

/* header */
.section-bar{position:absolute;left:0;top:11px;width:296px;height:17px;background:var(--brand-blue);color:#fff;font-size:11.2px;font-weight:600;line-height:17px;padding-left:18px;white-space:nowrap}
.brand-tag{position:absolute;left:304px;top:11px;display:flex;align-items:center;gap:4px;height:17px}
.brand-tag .mark{width:9px;height:9px;background:var(--brand-blue)}
.brand-tag .name{color:var(--brand-blue);font-size:5.4px;font-weight:600;line-height:6px;letter-spacing:.4px}

/* footer */
.page-num{position:absolute;left:8px;top:194px;font-size:6.5px;font-weight:600;color:var(--brand-blue)}
.foot-rule{position:absolute;left:20px;top:201px;width:337px;height:1px;background:var(--rule-blue)}
.foot-mark{position:absolute;left:359px;top:193px;width:10px;height:10px;border:1.4px solid var(--brand-blue);border-radius:2px}

/* content */
.content{position:absolute;left:21px}
.content h2{color:var(--brand-blue);font-size:12px;font-weight:700;margin-bottom:5px}
.content ul{list-style:none}
.content li{color:var(--ink-gray);font-size:8.8px;line-height:13.7px}
.content li::before{content:"• ";color:var(--brand-blue)}
.lead{position:absolute;color:var(--ink-gray);font-size:11.4px;line-height:14.4px}
.lead.big{font-size:12.6px;line-height:15px;font-weight:600;color:#6b6e72}
.photo{position:absolute}

/* cover */
.cover-band{position:absolute;left:0;top:99px;width:377px;height:113px;background:var(--brand-blue)}
.cover-tab{position:absolute;left:80px;top:0;width:217px;height:126px;background:#fff;border-bottom-right-radius:22px;display:flex;align-items:center;justify-content:center;padding-top:42px;gap:9px}
.cover-tab .mark{width:30px;height:30px;background:var(--brand-blue)}
.cover-tab .divider{width:1px;height:44px;background:var(--brand-blue)}
.cover-tab .name{color:var(--brand-blue);font-size:13.5px;line-height:15px;font-weight:400;letter-spacing:1.5px}
.cover-title{position:absolute;left:0;top:154px;width:377px;display:flex;align-items:center;gap:6px}
.cover-title .line{flex:1;height:1.5px;background:#fff}
.cover-title span{color:#fff;font-family:"Roboto",sans-serif;font-weight:700;font-size:15.5px;letter-spacing:.2px}
</style>
</head>
<body>

<!-- cover -->
<section class="slide c1 r1">
  <div class="cover-band"></div>
  <div class="cover-tab">
    <div class="mark"></div>
    <div class="divider"></div>
    <div class="name">HARLOW<br>COMMUNICATIONS</div>
  </div>
  <div class="cover-title"><div class="line"></div><span>MEDIA TRAINING</span><div class="line" style="flex:0 0 118px"></div></div>
</section>

<section class="slide c2 r1">
  <div class="section-bar">Section 1: Introduction to Media Training</div>
  <div class="brand-tag"><div class="mark"></div><div class="name">HARLOW<br>COMMUNICATIONS</div></div>
  <div class="content" style="top:61px">
    <h2>What is media training?</h2>
    <ul><li>It’s not natural.</li><li>It requires practice.</li><li>It’s about developing a mindset.</li></ul>
  </div>
  <div class="page-num">02</div><div class="foot-rule"></div><div class="foot-mark"></div>
</section>

<section class="slide c3 r1">
  <div class="section-bar">Section 1: Introduction to Media Training</div>
  <div class="brand-tag"><div class="mark"></div><div class="name">HARLOW<br>COMMUNICATIONS</div></div>
  <p class="lead" style="left:19px;top:57px;width:72px">Training and preparation are the difference between success and failure.</p>
  <svg class="photo" style="left:94px;top:37px" width="260" height="146" role="img" aria-label="Video still of a man in a suit being interviewed">
    <defs><linearGradient id="g3" x1="0" y1="0" x2="1" y2="1"><stop offset="0" stop-color="#8a6e5c"/><stop offset="1" stop-color="#3b3a3f"/></linearGradient></defs>
    <rect width="260" height="146" fill="url(#g3)"/>
  </svg>
  <div class="page-num">03</div><div class="foot-rule"></div><div class="foot-mark"></div>
</section>

<section class="slide c1 r2">
  <div class="section-bar">Section 1: Introduction to Media Training</div>
  <div class="brand-tag"><div class="mark"></div><div class="name">HARLOW<br>COMMUNICATIONS</div></div>
  <div class="content" style="left:24px;top:64px">
    <h2>Goals</h2>
    <ul><li>Learn how to prepare</li><li>Develop a strategy</li><li>Clarify message</li><li>Build a practice approach</li></ul>
  </div>
  <div class="page-num">04</div><div class="foot-rule"></div><div class="foot-mark"></div>
</section>

<section class="slide c2 r2">
  <div class="section-bar">Section 2: Preparation</div>
  <div class="brand-tag"><div class="mark"></div><div class="name">HARLOW<br>COMMUNICATIONS</div></div>
  <div class="content" style="left:18px;top:70px">
    <h2>What to negotiate?</h2>
    <ul><li>Timing and location</li><li>Rules of recording/broadcast</li><li>Rules of translation</li><li>Questions</li><li>Recording (for accuracy)</li></ul>
  </div>
  <svg class="photo" style="left:169px;top:48px" width="187" height="125" role="img" aria-label="Photo of an interviewer and guest shaking hands beside a camera">
    <defs><linearGradient id="g5" x1="0" y1="0" x2="1" y2="0"><stop offset="0" stop-color="#c9d3dd"/><stop offset="1" stop-color="#4a5664"/></linearGradient></defs>
    <rect width="187" height="125" fill="url(#g5)"/>
  </svg>
  <div class="page-num">05</div><div class="foot-rule"></div><div class="foot-mark"></div>
</section>

<section class="slide c3 r2">
  <div class="section-bar">Section 2: Preparation</div>
  <div class="brand-tag"><div class="mark"></div><div class="name">HARLOW<br>COMMUNICATIONS</div></div>
  <p class="lead big" style="left:15px;top:92px">Create<br>your story.</p>
  <svg class="photo" style="left:97px;top:41px" width="256" height="140" role="img" aria-label="Broadcast still of officials greeting schoolchildren">
    <defs><linearGradient id="g6" x1="0" y1="0" x2="0" y2="1"><stop offset="0" stop-color="#b9a49a"/><stop offset="1" stop-color="#a03a3e"/></linearGradient></defs>
    <rect width="256" height="140" fill="url(#g6)"/>
  </svg>
  <div class="page-num">06</div><div class="foot-rule"></div><div class="foot-mark"></div>
</section>

<section class="slide c1 r3">
  <div class="section-bar">Section 2: Preparation</div>
  <div class="brand-tag"><div class="mark"></div><div class="name">HARLOW<br>COMMUNICATIONS</div></div>
  <div class="content" style="left:24px;top:79px">
    <h2>On the record:</h2>
    <ul><li>Everything for print</li><li>Your name for attribution</li><li>Always assume everything is on the record</li></ul>
  </div>
  <div class="page-num">07</div><div class="foot-rule"></div><div class="foot-mark"></div>
</section>

<section class="slide c2 r3">
  <div class="section-bar">Section 2: Preparation</div>
  <div class="brand-tag"><div class="mark"></div><div class="name">HARLOW<br>COMMUNICATIONS</div></div>
  <div class="content" style="left:23px;top:79px">
    <h2>Off the record:</h2>
    <ul><li>Not for print</li><li>Not for attribution</li><li>Doesn’t mean it won’t be used/printed</li></ul>
  </div>
  <div class="page-num">08</div><div class="foot-rule"></div><div class="foot-mark"></div>
</section>

<section class="slide c3 r3">
  <div class="section-bar">Section 2: Preparation</div>
  <div class="brand-tag"><div class="mark"></div><div class="name">HARLOW<br>COMMUNICATIONS</div></div>
  <div class="content" style="left:23px;top:79px">
    <h2>On Background:</h2>
    <ul><li>Education</li><li>Context for print</li><li>Can be used with attribution</li><li>Attribution to be negotiated</li></ul>
  </div>
  <div class="page-num">09</div><div class="foot-rule"></div><div class="foot-mark"></div>
</section>

<section class="slide c1 r4">
  <div class="section-bar">Section 2: Preparation</div>
  <div class="brand-tag"><div class="mark"></div><div class="name">HARLOW<br>COMMUNICATIONS</div></div>
  <p class="lead big" style="left:17px;top:96px">Preparation<br>Matters!</p>
  <svg class="photo" style="left:95px;top:38px" width="264" height="144" role="img" aria-label="Video clip of a televised sit-down interview on a studio set">
    <defs><radialGradient id="g10" cx=".5" cy=".5" r=".6"><stop offset="0" stop-color="#7a2a24"/><stop offset="1" stop-color="#150d0c"/></radialGradient></defs>
    <rect width="264" height="144" fill="url(#g10)"/>
  </svg>
  <div class="page-num">10</div><div class="foot-rule"></div><div class="foot-mark"></div>
</section>

<section class="slide c2 r4">
  <div class="section-bar">Section 2: Preparation</div>
  <div class="brand-tag"><div class="mark"></div><div class="name">HARLOW<br>COMMUNICATIONS</div></div>
  <div class="content" style="left:23px;top:77px">
    <h2>Schedule</h2>
    <ul><li>Develop Q/A</li><li>Write answers but also vocalize</li><li>Practice: table</li><li>Practice: mock</li></ul>
  </div>
  <div class="page-num">11</div><div class="foot-rule"></div><div class="foot-mark"></div>
</section>

<section class="slide c3 r4">
  <div class="section-bar">Section 2: Preparation</div>
  <div class="brand-tag"><div class="mark"></div><div class="name">HARLOW<br>COMMUNICATIONS</div></div>
  <div class="content" style="left:23px;top:77px">
    <h2>Go Wider</h2>
    <ul><li>Know recent news</li><li>Know your footprint</li><li>Know upcoming events</li></ul>
  </div>
  <div class="page-num">12</div><div class="foot-rule"></div><div class="foot-mark"></div>
</section>

</body>
</html>
```